Glossy black background with white text, image of webcam on right.

Text:

YOU HAVE BEEN CHOSEN
to be a Camgirl online model!

- earn $10,000/month from home
- choose your own hours

Meridian Lowe
The Halvard

Dennis Pallot
Director
VELORIX PTY LTD
mob 0491 302184
email sales@velorixhq.com

www.VELORIXHQ.com

the Lowe signature can go on the back.

Meridian Lowe
The Halvard

thanks

On the front: the webcam image should be quite large

On the back: Lowe sig with an apple image or icon

good luck!

On the back should be in cursive with a small apple picture. (green)

Lowe
The Halvard

no "meridian"

Target Market(s)

young hot women

Requirements
Must have
• "You Have Been Chosen"
in the largest font
Nice to have
• see attached photo of webcam
maybe some yellow text
Should not have
• consider removing logo from webcam pic

```html
<!DOCTYPE html>
<html lang="en">
<head>
<meta charset="utf-8">
<title>Velorix Business Card</title>
<link rel="stylesheet" href="https://fonts.googleapis.com/css2?family=Saira+Semi+Condensed:wght@600&family=Noto+Sans:wght@500;700&family=Cormorant+Garamond:ital,wght@1,500&display=swap">
<style>
  :root {
    --page: #ffffff;
    --card: #060606;
    --white: #ffffff;
    --yellow: #f2e600;
    --orange: #ffa640;
    --glow: #d8321a;
    --cam-dark: #0b0b0b;
    --cam-mid: #3a3a3a;
    --cam-light: #8a8a8a;
  }
  * { margin: 0; padding: 0; box-sizing: border-box; }
  html, body {
    width: 1200px; height: 364px; overflow: hidden;
    background: var(--page);
  }
  .card {
    position: absolute; top: 0; height: 364px;
    background: var(--card); overflow: hidden;
  }
  .card--front { left: 0; width: 583px; }
  .card--back { left: 618px; width: 582px; }

  .webcam-photo {
    position: absolute;
    background:
      radial-gradient(circle at 42% 36%, var(--cam-dark) 0 14%, var(--cam-light) 16%, var(--cam-dark) 19%, var(--cam-mid) 34%, #1a1a1a 48%, transparent 62%),
      radial-gradient(ellipse at 45% 85%, #6a6a6a 0, #222 25%, transparent 45%),
      var(--cam-dark);
  }
  .card--front .webcam-photo { left: 259px; top: 59px; width: 324px; height: 241px; }
  .card--back .webcam-photo { left: 0; top: 48px; width: 323px; height: 242px; }

  .headline {
    position: absolute; left: 14px; top: 22px;
  }
  .headline text {
    font-family: "Saira Semi Condensed", sans-serif;
    font-weight: 600; font-size: 52px; fill: var(--white);
  }
  .subline {
    position: absolute; left: 106px; top: 77px;
    font-family: Arial, "Noto Sans", sans-serif;
    font-size: 20px; color: var(--white); line-height: 24px;
  }
  .perks {
    position: absolute; left: 20px; top: 146px;
    font-family: "Noto Sans", sans-serif; font-weight: 700;
    font-size: 19px; line-height: 22.5px; color: var(--orange);
    text-shadow: 0 0 2px var(--glow), 0 0 3px var(--glow);
    list-style: none;
  }
  .contact {
    position: absolute;
    font-family: "Noto Sans", sans-serif; font-weight: 500;
    font-size: 14.5px; line-height: 16.6px; color: var(--yellow);
    font-style: normal;
  }
  .card--front .contact { left: 200px; top: 251px; }
  .card--back .contact { left: 372px; top: 247px; }
  .contact .web { font-family: Arial, "Noto Sans", sans-serif; font-weight: 400; }

  .signature {
    position: absolute; left: 369px; top: 134px;
    font-family: "Cormorant Garamond", serif; font-style: italic; font-weight: 500;
    font-size: 33px; line-height: 39px; color: var(--white);
  }
</style>
</head>
<body>
  <section class="card card--front">
    <div class="webcam-photo" role="img" aria-label="Close-up photograph of a black webcam"></div>
    <svg class="headline" width="460" height="50" aria-label="YOU HAVE BEEN CHOSEN">
      <text x="0" y="43" textLength="453" lengthAdjust="spacingAndGlyphs">YOU HAVE BEEN CHOSEN</text>
    </svg>
    <p class="subline">to be a Camgirl online model!</p>
    <ul class="perks">
      <li>Earn $10,000/month from home</li>
      <li>Choose your own hours</li>
    </ul>
    <address class="contact">
      Dennis Pallot<br>
      Director<br>
      VELORIX PTY LTD<br>
      mob 0491 302184<br>
      email sales@velorixhq.com<br>
      <span class="web">www.VELORIXHQ.com</span>
    </address>
  </section>

  <section class="card card--back">
    <div class="webcam-photo" role="img" aria-label="Close-up photograph of a black webcam"></div>
    <p class="signature">Lowe<br>The Halvard</p>
    <address class="contact">
      Dennis Pallot<br>
      Director<br>
      VELORIX PTY LTD<br>
      mob 0491 302184<br>
      email sales@velorixhq.com<br>
      <span class="web">www.VELORIXHQ.com</span>
    </address>
  </section>
</body>
</html>
```